Flyer-Design für  junges, dynamisches Unternehmen, spezialisiert auf innovative Trainingskonzepte
Flyer-Design für junges, dynamisches Unternehmen, spezialisiert auf innovative Trainingskonzepte
dqlVIT
Sehr kreative und ideenreiche Umsetzungen. Alle Wünsche sind sehr sorgfältig, gewissenhaft und mit absoluter Schnelligkeit erfolgt.
Zielgruppe
Als junges dynamisches Unternehmen ist dqlVIT spezialisiert auf innovative Trainingskonzepte. Wir sind
ein international anerkanntes Trainingscenter der Northfield Rescue Alliance und bieten Notfalltrainings,
Erste-Hilfe-Kurse sowie hochwertige Simulationstrainings fur Rettungsdienste und Krankenhäuser an. In
unseren CRM- Simulationstrainings coachen wir Notfallteams in den Bereichen Skills, Human Factor und
Kommunikation. Hierbei kommen Full-Scale-Simulatoren und Schauspielpatienten zum Einsatz, die eine
realitätsnahe und lebensechte Trainingssituation präsentieren.
Aufgabenstellung
Wir suchen zur Vermarktung unserer Kurse eine graphische Übersicht, aus der die Qualitätsmerkmale von dqlVIT, eine Zielgruppen definition sowie eine detailierte Aufarbeitung der Kursinhalte in den Verschiedenen Kursformaten hervorgeht und unsere zukünftigen Kunden von uns überzeugt.
Großer Fokus dieses Projektes, ist es die Innenseite des Flyers zu gestalten, die ein geschlossenes Gesamtbild aufweisen soll. Deckblatt und Rückseite sind nebensächlich, hier freuen wir uns über neue Ideen, aber das Fokus ist die Gestaltung der Innenseite.

```html
<!DOCTYPE html>
<html lang="de">
<head>
<meta charset="utf-8">
<title>dqlVIT – Kursübersicht Innenseite</title>
<link rel="stylesheet" href="https://fonts.googleapis.com/css2?family=Exo+2:ital,wght@1,700;1,800&family=PT+Sans:ital,wght@0,400;0,700;1,400;1,700&family=PT+Sans+Narrow:wght@400;700&family=Permanent+Marker&display=swap">
<style>
  :root{
    --red:#d81f26;
    --red-dark:#8e1418;
    --red-deep:#a5161b;
    --gray-band:#55575a;
    --panel:#e5e6e8;
    --text:#3b3b3d;
    --line:#6b6b6b;
    --light-a:#fbe39a; --light-b:#e6ad45;
    --basic-a:#eea460; --basic-b:#c8690f;
    --prem-a:#ececec; --prem-b:#b3b4b6;
    --plus-a:#ffe600; --plus-b:#eeae00;
  }
  *{margin:0;padding:0;box-sizing:border-box}
  html,body{width:1200px;height:849px;overflow:hidden;background:#fff}
  .spread{position:relative;width:1200px;height:849px;overflow:hidden;background:#fff;font-family:"PT Sans",sans-serif;color:var(--text)}
  .band{position:absolute;left:0;width:1200px}
  .band--top{top:0;height:50px}
  .band--bottom{top:770px;height:79px}

  .advantages__title{position:absolute;left:35px;top:60px;font:italic 800 16.5px "Exo 2",sans-serif;color:var(--red)}
  .advantages__card{position:absolute;left:150px;top:88px;width:449px;height:263px;box-shadow:3px 4px 8px rgba(0,0,0,.14);background:#fff}
  .strip{position:absolute;height:21px;background:linear-gradient(90deg,var(--red-deep),var(--red));color:#fff;font:italic 7.6px "Permanent Marker",sans-serif;line-height:21px;white-space:nowrap}
  .strip--left{left:62px;padding-left:32px;clip-path:polygon(0 0,calc(100% - 21px) 0,100% 100%,0 100%)}
  .strip--right{padding-right:34px;text-align:right;clip-path:polygon(0 0,100% 0,100% 100%,21px 100%)}
  .badge{position:absolute;width:54px;height:54px;border-radius:50%;background:var(--red-dark);display:flex;align-items:center;justify-content:center}
  .badge svg{width:32px;height:32px;fill:none;stroke:#fff;stroke-width:1.6;stroke-linecap:round;stroke-linejoin:round}

  .partners__lead{position:absolute;left:35px;top:358px;font:italic 400 11.5px "PT Sans",sans-serif;color:var(--red)}
  .partner{position:absolute;width:200px;text-align:center;font:700 9.6px/12px "PT Sans Narrow",sans-serif;color:#444}
  .partner__seal{display:block;width:57px;height:57px;margin:0 auto 8px;border:1px solid #333;border-radius:50%}

  .courses{position:absolute;left:0;top:487px;width:600px;height:188px;background:var(--panel);padding:21px 35px 0}
  .courses p{font-size:10.4px;line-height:13.1px;margin-bottom:13px;width:510px}
  .courses strong{font:italic 700 12px "PT Sans",sans-serif;color:var(--red)}

  .photo{position:absolute;top:674px;height:170px}
  .photo--1{left:0;width:190px;background:linear-gradient(160deg,#c9c2bd,#7a6f6b 50%,#a6534a)}
  .photo--2{left:199px;width:198px;background:linear-gradient(150deg,#8c8580,#5d5551 45%,#b8483a)}
  .photo--3{left:407px;width:193px;background:linear-gradient(140deg,#3c3a3a,#8f4a3e 55%,#c3382c)}

  .web{position:absolute;left:1006px;top:817px;font:italic 700 18px "Exo 2",sans-serif;color:#fff;letter-spacing:.3px}

  /* course overview, built horizontally then turned to read top-down */
  .overview{position:absolute;left:1160px;top:31px;width:742px;height:460px;transform-origin:0 0;transform:rotate(90deg)}
  .overview__lines{position:absolute;left:0;top:0}
  .overview__title{position:absolute;left:28px;top:10px;font:italic 800 26px "Exo 2",sans-serif;color:var(--red);white-space:nowrap}
  .overview__note{position:absolute;left:222px;top:426px;font:italic 400 10px "PT Sans",sans-serif;color:#555;white-space:nowrap}
  .tier{position:absolute;height:34px;display:flex;align-items:center;justify-content:center;font:700 14px "PT Sans Narrow",sans-serif;color:#fff;box-shadow:2px 2px 3px rgba(0,0,0,.15)}
  .tier--light{background:linear-gradient(0deg,var(--light-b),var(--light-a))}
  .tier--basic{background:linear-gradient(0deg,var(--basic-b),var(--basic-a))}
  .tier--premium{background:linear-gradient(0deg,var(--prem-b),var(--prem-a))}
  .tier--plus{background:linear-gradient(0deg,var(--plus-b),var(--plus-a))}
  .tier__info{position:absolute;top:121px;font:700 7.4px "PT Sans Narrow",sans-serif;color:#222;white-space:nowrap}
  .item{position:absolute;height:34px;border:1px solid var(--red);background:#fff;padding:3px 7px;font:400 6.4px/7.4px "PT Sans Narrow",sans-serif;color:#222;box-shadow:1px 2px 3px rgba(0,0,0,.12)}
  .item--wide{height:83px}
</style>
</head>
<body>
<div class="spread">

  <svg class="band band--top" viewBox="0 0 1200 50" aria-hidden="true">
    <path d="M0 0H930C700 8 320 20 0 27Z" fill="#c2181f"/>
    <path d="M0 27C320 20 600 14 780 16C560 23 260 34 0 45Z" fill="var(--gray-band)"/>
  </svg>

  <h2 class="advantages__title">Was sind unsere Vorteile/Was zeichnet dqlVIT aus?</h2>
  <div class="advantages__card"></div>

  <div class="strip strip--left" style="top:108px;width:275px">- Zertifizierte und anerkannte Kurskonzepte</div>
  <div class="strip strip--right" style="left:193px;top:136px;width:345px">- Angenehme Lernatmosphäre mit emphatischen Instruktoren</div>
  <div class="strip strip--left" style="top:163px;width:348px">- Realistische Aus- und Fortbildung mit Schauspielpatienten</div>
  <div class="strip strip--right" style="left:253px;top:190px;width:285px">- Modernstes Material, Technik und Simulatoren</div>
  <div class="strip strip--left" style="top:218px;width:381px">- Alle Dozenten mit langjähriger Erfahrung in der Notfallmedizin</div>
  <div class="strip strip--right" style="left:233px;top:245px;width:305px">- Praxisorientierte und individuelle Kursgestaltung</div>
  <div class="strip strip--left" style="top:272px;width:387px">- Durchführung der Schulungen bei unseren Kunden inhouse vor Ort</div>
  <div class="strip strip--right" style="left:178px;top:300px;width:360px">- Förderung der Teamarbeit durch Crew Ressource Management</div>

  <div class="badge" style="left:35px;top:92px"><svg viewBox="0 0 32 32"><rect x="8" y="6" width="20" height="13"/><path d="M11 16l5-4 4 2 5-5M6 10v8l4 3v6M4 27h10"/></svg></div>
  <div class="badge" style="left:511px;top:119px"><svg viewBox="0 0 32 32"><path d="M16 25c-6-4-9-7-9-11a4 4 0 0 1 9-2 4 4 0 0 1 9 2c0 4-3 7-9 11Z"/><path d="M4 18c2 5 6 9 12 10 6-1 10-5 12-10"/></svg></div>
  <div class="badge" style="left:35px;top:146px"><svg viewBox="0 0 32 32"><circle cx="10" cy="7" r="3"/><circle cx="22" cy="7" r="3"/><path d="M7 28V12h6v16M19 28V12h6v16M13 16h6"/></svg></div>
  <div class="badge" style="left:511px;top:173px"><svg viewBox="0 0 32 32"><path d="M16 3c4 4 5 9 4 15h-8c-1-6 0-11 4-15Z"/><circle cx="16" cy="11" r="2"/><path d="M12 18l-4 5h5M20 18l4 5h-5M14 22l2 6 2-6"/></svg></div>
  <div class="badge" style="left:35px;top:201px"><svg viewBox="0 0 32 32"><rect x="4" y="4" width="7" height="6"/><rect x="21" y="4" width="7" height="6"/><circle cx="16" cy="16" r="3"/><path d="M11 7l3 6M21 7l-3 6M10 28v-5a6 6 0 0 1 12 0v5"/></svg></div>
  <div class="badge" style="left:511px;top:228px"><svg viewBox="0 0 32 32"><circle cx="14" cy="14" r="10"/><path d="M14 8v6l4 3"/><circle cx="23" cy="23" r="6"/><path d="M21 21h3v4"/></svg></div>
  <div class="badge" style="left:35px;top:256px"><svg viewBox="0 0 32 32"><circle cx="14" cy="13" r="9"/><path d="M14 8v5h4"/><rect x="15" y="19" width="13" height="8"/><circle cx="18" cy="28" r="1.5"/><circle cx="25" cy="28" r="1.5"/></svg></div>
  <div class="badge" style="left:511px;top:283px"><svg viewBox="0 0 32 32"><circle cx="16" cy="6" r="3"/><path d="M13 14h6M16 9v6M16 15v4M8 19h16M8 19v3M24 19v3"/><circle cx="8" cy="25" r="2.5"/><circle cx="24" cy="25" r="2.5"/></svg></div>

  <p class="partners__lead">Wir sind ….</p>
  <div class="partner" style="left:16px;top:380px"><span class="partner__seal"></span>International anerkanntes Trainingscenter<br>der Northfield Rescue Alliance</div>
  <div class="partner" style="left:206px;top:380px"><span class="partner__seal"></span>Partner und Förderer der SIMVERA e.V.</div>
  <div class="partner" style="left:400px;top:380px"><span class="partner__seal"></span>Modernes Training unter Einsatz<br>von Video-Debriefing</div>

  <section class="courses">
    <p><strong>Notfalltraining Light -</strong> Lernen Sie in diesem Skilltraining die Reanimation und beherrschen Sie die Herzdruckmassage. Außerdem besprechen wir die Intubation und die Defibrillation mit einem AED.</p>
    <p><strong>Notfalltraining Basic -</strong> Interaktives Team-Training: Üben Sie die wichtigsten Handgriffe und lernen Sie Ihre eigene Notfallausrüstung kennen. Das medizinische Know-How wird durch zusätzliche Themen wie Teamwork und Kommunikation erweitert.</p>
    <p><strong>Notfalltraining Premium -</strong> Weg mit der Puppe! Wir bringen unseren Schauspielpatienten mit zu Ihnen! Wir trainieren dynamische Notfälle und gemeinsam mit Ihnen analysieren und optimieren wir Ihr Notfallmanagement in Ihrer Praxis. Mit diesem Training schaffen Sie eine hohe Zufriedenheit mit Ihren Mitarbeitern und sind perfekt auf den nächsten Notfall vorbereitet. Auf Wunsch bieten wir Ihnen eine kostenlose Beratung und Verwaltung Ihrer Notfallausrüstung an.</p>
  </section>

  <div class="photo photo--1" role="img" aria-label="Foto: Herzdruckmassage an einer Simulationspuppe mit Monitor im Hintergrund"></div>
  <div class="photo photo--2" role="img" aria-label="Foto: Team versorgt einen Simulationspatienten mit Beatmung"></div>
  <div class="photo photo--3" role="img" aria-label="Foto: Rettungsteam beatmet einen Schauspielpatienten am Boden"></div>

  <svg class="band band--bottom" viewBox="0 0 1200 79" aria-hidden="true">
    <path d="M407 40C700 26 950 14 1200 9V22C950 25 700 33 407 42Z" fill="var(--gray-band)"/>
    <path d="M0 72C400 55 800 33 1200 24V79H0Z" fill="#c2181f"/>
  </svg>
  <div class="web">www.dqlVIT.de</div>

  <section class="overview">
    <svg class="overview__lines" width="742" height="460" viewBox="0 0 742 460" fill="none" stroke="var(--line)" stroke-width="1">
      <path d="M5.6 100V406M5.6 100H27.5M5.6 162H27.5M5.6 211H27.5M5.6 260H27.5M5.6 309H27.5M5.6 358H27.5M5.6 407H27.5"/>
      <path d="M193.7 100V438.8M193.7 100H214M193.7 162H214M193.7 211H214M193.7 260H214M193.7 309H214M193.7 358H214"/>
      <path d="M379.2 100V449.3M379.2 100H399M379.2 162H399M379.2 211H399M379.2 284H399"/>
      <path d="M564.8 100V458.1M564.8 100H587M564.8 162H587M564.8 211H587M564.8 284H587"/>
      <path d="M98.6 438.8H193.7M98.6 449.3H379.2M98.6 458.1H564.8"/>
      <path d="M98.6 423.1V458.1M283.6 374.5V458.1M470.7 325.4V458.1"/>
    </svg>

    <h2 class="overview__title">Kursdetails &amp; Preise</h2>
    <p class="overview__note">*Beinhaltet immer die vorrausgehenden Kurspackete</p>

    <div class="tier tier--light" style="left:27.5px;top:83px;width:142.5px">Light</div>
    <div class="tier__info" style="left:27.5px">2Std. | BLS | 1 Instruktor: 123,- €</div>
    <div class="item" style="left:27.5px;top:145px;width:142.5px">Vorstellungen und Erläuterung des Basic-Life-Support für med. Fachpersonal</div>
    <div class="item" style="left:27.5px;top:194px;width:142.5px">Auffinden eines bewusstlosen Patienten</div>
    <div class="item" style="left:27.5px;top:243px;width:142.5px">High-Performance-Reanimation, 5 Kriterien für eine perfekte Herz-Druck-Massage</div>
    <div class="item" style="left:27.5px;top:292px;width:142.5px">Vorstellung Beutel-Masken-Beatmung, LTtubus und Pocketmaske</div>
    <div class="item" style="left:27.5px;top:341px;width:142.5px">Vorstellung und Anwendung AED (Defi)</div>
    <div class="item" style="left:27.5px;top:390px;width:142.5px">Trainingsszenarien zum Ablauf einer Reanimation</div>

    <div class="tier tier--basic" style="left:214px;top:83px;width:143px">Basic*</div>
    <div class="tier__info" style="left:214px">3 Std. | 1 Instruktor | BLS + CRM: 234,- €</div>
    <div class="item" style="left:214px;top:145px;width:143px">Übungen zur Beatmung für jeden Teilnehmer</div>
    <div class="item" style="left:214px;top:194px;width:143px">Übungen mit dem AED für jeden Teilnehmer</div>
    <div class="item" style="left:214px;top:243px;width:143px">Elektronische Auswertung der Reanimationsergebnisse</div>
    <div class="item" style="left:214px;top:292px;width:143px">Training zur Teamkoordination und Teamkommunikation</div>
    <div class="item" style="left:214px;top:341px;width:143px">Fallbeispiele zur Reanimation mit Feedback zur Aufgabenbewältigung und Kommunikation</div>

    <div class="tier tier--premium" style="left:399px;top:83px;width:143px">Premium*</div>
    <div class="tier__info" style="left:399px">4 Std. | 1 Instruktor | BLS+CRM: 456,- €</div>
    <div class="item" style="left:399px;top:145px;width:143px">Überprüfung und auf Wunsch Anpassung der internen Abläufe der Rettungskette (QM/Notfallplan)</div>
    <div class="item" style="left:399px;top:194px;width:143px">Fallbeispieltraining mit echtem Patienten (Schauspieler)</div>
    <div class="item item--wide" style="left:399px;top:243px;width:143px">Fallbeispiel zu ausgewählten und passenden Themen wie Asthma, Anaphylaxie, Krampfanfall, Bolusgeschehen, Herzinfarkt, etc. die Auswahl erfolgt anhand der Fachrichtung/Praxisschwerpunkt</div>

    <div class="tier tier--plus" style="left:587px;top:83px;width:142px">PremiumPLUS*</div>
    <div class="tier__info" style="left:587px">Ab 4 Std. | 2 Intruktoren | BLS+ALS+CRM: 7890,- €</div>
    <div class="item" style="left:587px;top:145px;width:142px">ABCDE-Schema zur Ersteinschätzung von kritisch kranken Patienten</div>
    <div class="item" style="left:587px;top:194px;width:142px">FORDEC-Training zur Entscheidungsfindung</div>
    <div class="item item--wide" style="left:587px;top:243px;width:142px">Fallbeispiele zu lebensbedrohlichen Situationen mit einem High-Tech-Simulator u.a. mit Sprachfunktion, realistischen Atembewegungen mit Atemgeräuschen, Zyanose, tastebaren Pulsen und der Durchführung von Maßnahmen (z.B.: Entlastungspunktion, Infusionstherapie, etc.)</div>
  </section>

</div>
</body>
</html>
```